Velaski Law Firm
Project: Stationary for Law Firm
Stationary for Law Firm - Law
Stationary for Law Firm
Professional
Tomas Edgar Velaski
Attorney / Abogado
418 W. Brambleton Ave Bldg. 3. Suite 560 Charlotte, NC 28790
info@velaskilawfirm.example
www.velaskilawfirm.example
IMMIGRATION LAW
Logo and "Immigration Law"
Brisko Brisko
velaskilawfirm velaskilawfirm
Please also submit drafts for letterhead and envelopes. Thank you.

```html
<!DOCTYPE html>
<html lang="en">
<head>
<meta charset="utf-8">
<title>Velaski Law Firm — Stationery</title>
<link href="https://fonts.googleapis.com/css2?family=Lato:wght@300;400;700&display=swap" rel="stylesheet">
<style>
  :root {
    --navy: #0d1f6b;
    --blue: #1f3bb0;
    --blue-light: #3d5fd8;
    --paper: #ffffff;
    --ink: #333a4a;
    --muted: #8a90a0;
    --ghost: rgba(13, 31, 107, 0.055);
    --ghost-light: rgba(255, 255, 255, 0.07);
    --stage: #d9dbe0;
    --stage-edge: #b9bcc4;
    --caption: #555a66;
  }
  * { margin: 0; padding: 0; box-sizing: border-box; }
  html, body { width: 1200px; height: 329px; overflow: hidden; }
  body {
    font-family: "Lato", Arial, sans-serif;
    color: var(--ink);
    background: radial-gradient(ellipse at 50% 45%, #f2f3f5 0%, var(--stage) 60%, var(--stage-edge) 100%);
    position: relative;
  }
  .piece { position: absolute; background: var(--paper); box-shadow: 0 2px 6px rgba(0,0,0,.18); overflow: hidden; }
  .caption { position: absolute; font-size: 6px; color: var(--caption); text-align: center; letter-spacing: .3px; }

  .brand { display: flex; align-items: center; gap: 4px; font-weight: 700; color: var(--navy); text-transform: uppercase; letter-spacing: .5px; white-space: nowrap; }
  .brand .mark { background: var(--navy); display: inline-block; flex: none; }
  .brand.on-dark { color: #fff; }
  .brand.on-dark .mark { background: #fff; }

  /* faint name used as background decoration */
  .ghost-name {
    position: absolute; font-weight: 700; text-transform: uppercase;
    color: var(--ghost); line-height: .95; text-align: center; letter-spacing: 1px;
    white-space: nowrap; pointer-events: none;
  }
  .ghost-name.on-dark { color: var(--ghost-light); }

  /* Letterhead */
  .letterhead { width: 204px; height: 264px; top: 34px; }
  .letterhead .brand { position: absolute; top: 14px; right: 16px; font-size: 7px; }
  .letterhead .brand .mark { width: 10px; height: 10px; }
  .letterhead .contact { position: absolute; top: 12px; left: 16px; font-size: 3.6px; line-height: 5px; color: var(--muted); }
  .letterhead .rule { position: absolute; top: 32px; left: 16px; right: 16px; height: 1px; background: var(--blue); }
  .letterhead .ghost-name { right: 10px; top: 150px; font-size: 30px; text-align: right; }
  .letterhead .body { position: absolute; top: 44px; left: 16px; right: 16px; font-size: 4.5px; line-height: 6.6px; color: var(--ink); }
  .letterhead .body p { margin-bottom: 5px; }
  .letterhead .sign { position: absolute; bottom: 24px; left: 16px; font-size: 4.5px; line-height: 6px; }
  .letterhead .sign strong { color: var(--navy); display: block; }
  .letterhead .footer { position: absolute; bottom: 0; left: 0; right: 0; height: 8px; background: linear-gradient(90deg, var(--navy), var(--blue-light)); }

  /* Business card */
  .card { left: 473px; top: 108px; width: 116px; height: 62px; display: flex; }
  .card .front { width: 50%; display: flex; align-items: center; justify-content: center; border-right: 1px solid #e6e8ee; }
  .card .front .brand { font-size: 4.6px; flex-direction: column; gap: 3px; }
  .card .front .mark { width: 12px; height: 12px; }
  .card .back { width: 50%; padding: 7px 4px; font-size: 3.1px; line-height: 4.4px; color: var(--muted); }
  .card .back strong { color: var(--navy); font-size: 4.2px; display: block; }
  .card .back .title { color: var(--blue); margin-bottom: 3px; display: block; }
  .card .stripe { position: absolute; bottom: 0; left: 0; right: 0; height: 4px; background: var(--blue); }

  /* Envelope */
  .envelope { left: 478px; top: 196px; width: 124px; height: 84px;
    background: radial-gradient(ellipse at 30% 40%, var(--blue-light), var(--navy) 80%); }
  .envelope .brand { position: absolute; top: 10px; left: 10px; font-size: 5px; }
  .envelope .brand .mark { width: 8px; height: 8px; }
  .envelope .address { position: absolute; top: 21px; left: 10px; font-size: 3.2px; line-height: 4.4px; color: #cfd8ff; }
  .envelope .ghost-name { right: 6px; bottom: 6px; font-size: 13px; text-align: right; }

  /* Folder front */
  .folder-front { left: 640px; top: 28px; width: 208px; height: 272px; }
  .folder-front .top { position: absolute; inset: 0 0 42% 0; background: linear-gradient(180deg, #fff, #f0f2f6); }
  .folder-front .top .ghost-name { left: 0; right: 0; top: 40px; font-size: 34px; }
  .folder-front .bottom { position: absolute; left: 0; right: 0; bottom: 0; height: 42%;
    background: radial-gradient(ellipse at 50% 30%, var(--blue-light), var(--navy) 75%);
    display: flex; flex-direction: column; align-items: center; justify-content: center; gap: 6px; }
  .folder-front .brand { font-size: 10px; }
  .folder-front .brand .mark { width: 14px; height: 14px; }
  .folder-front .tag { font-size: 5px; letter-spacing: 2px; color: #cfd8ff; }

  /* Folder inside */
  .folder-inside { left: 866px; top: 28px; width: 312px; height: 272px; display: flex; background: transparent; }
  .panel { position: relative; width: 50%; height: 100%; background: linear-gradient(180deg, #fff, #eef0f5); overflow: hidden; }
  .panel + .panel { border-left: 1px solid #d5d8e0; }
  .panel .pocket { position: absolute; left: 0; right: 0; bottom: 0; height: 36%;
    background: radial-gradient(ellipse at 50% 20%, var(--blue-light), var(--navy) 80%); }
  .panel .ghost-name { left: 0; right: 0; top: 44px; font-size: 26px; }
  .panel .slot { position: absolute; left: 50%; bottom: 28px; width: 58px; height: 32px; margin-left: -29px; background: #fff; padding: 5px; }
  .panel .slot .brand { font-size: 3.6px; gap: 2px; }
  .panel .slot .mark { width: 6px; height: 6px; }
  .panel .slot small { display: block; font-size: 3px; color: var(--muted); margin-top: 4px; line-height: 4px; }
  .panel .slit { position: absolute; left: 50%; bottom: 62px; width: 70px; height: 1px; margin-left: -35px; background: rgba(255,255,255,.5); }
</style>
</head>
<body>

  <!-- Letterhead front -->
  <section class="piece letterhead" style="left:24px">
    <div class="contact">418 W. Brambleton Ave Bldg. 3. Suite 560<br>Charlotte, NC 28790<br>info@velaskilawfirm.example</div>
    <div class="brand"><span class="mark"></span>Velaski Law Firm</div>
    <div class="rule"></div>
    <div class="ghost-name" aria-hidden="true">Velaski<br>Law Firm</div>
    <div class="body">
      <p>Client Name<br>Company Address</p>
      <p>Dear Client,</p>
      <p>We write to confirm the details of your case and the next steps our team will take on your behalf.</p>
      <p>Please review the enclosed documents carefully and sign where marked. Return them to our office at your earliest convenience so we may proceed.</p>
      <p>Should you have any questions, our staff is available during regular office hours to assist you.</p>
      <p>Sincerely,</p>
    </div>
    <div class="sign"><strong>Tomas Edgar Velaski</strong>Attorney / Abogado</div>
    <div class="footer"></div>
  </section>
  <div class="caption" style="left:24px;top:304px;width:204px">Letterhead Front</div>

  <!-- Letterhead back -->
  <section class="piece letterhead" style="left:240px">
    <div class="contact">418 W. Brambleton Ave Bldg. 3. Suite 560<br>Charlotte, NC 28790<br>www.velaskilawfirm.example</div>
    <div class="brand"><span class="mark"></span>Velaski Law Firm</div>
    <div class="rule"></div>
    <div class="ghost-name" aria-hidden="true">Velaski<br>Law Firm</div>
    <div class="body">
      <p>Client Name<br>Company Address</p>
      <p>Dear Client,</p>
      <p>We write to confirm the details of your case and the next steps our team will take on your behalf.</p>
      <p>Please review the enclosed documents carefully and sign where marked. Return them to our office at your earliest convenience so we may proceed.</p>
      <p>Should you have any questions, our staff is available during regular office hours to assist you.</p>
      <p>Sincerely,</p>
    </div>
    <div class="sign"><strong>Tomas Edgar Velaski</strong>Attorney / Abogado</div>
    <div class="footer"></div>
  </section>
  <div class="caption" style="left:240px;top:304px;width:204px">Letterhead Back</div>

  <!-- Business card -->
  <section class="piece card">
    <div class="front"><div class="brand"><span class="mark"></span>Velaski Law Firm</div></div>
    <div class="back">
      <strong>Tomas Edgar Velaski</strong>
      <span class="title">Attorney / Abogado</span>
      418 W. Brambleton Ave Bldg. 3. Suite 560<br>Charlotte, NC 28790<br>info@velaskilawfirm.example<br>www.velaskilawfirm.example
    </div>
    <div class="stripe"></div>
  </section>
  <div class="caption" style="left:473px;top:174px;width:116px">Business Card</div>

  <!-- Envelope -->
  <section class="piece envelope">
    <div class="brand on-dark"><span class="mark"></span>Velaski Law Firm</div>
    <div class="address">418 W. Brambleton Ave Bldg. 3. Suite 560<br>Charlotte, NC 28790</div>
    <div class="ghost-name on-dark" aria-hidden="true">Velaski<br>Law Firm</div>
  </section>
  <div class="caption" style="left:478px;top:285px;width:124px">Envelope Design</div>

  <!-- Folder front -->
  <section class="piece folder-front">
    <div class="top"><div class="ghost-name" aria-hidden="true">Velaski<br>Law Firm</div></div>
    <div class="bottom">
      <div class="brand on-dark"><span class="mark"></span>Velaski Law Firm</div>
      <div class="tag">IMMIGRATION LAW</div>
    </div>
  </section>
  <div class="caption" style="left:640px;top:304px;width:208px">Folder Front</div>

  <!-- Folder inside -->
  <section class="piece folder-inside">
    <div class="panel">
      <div class="pocket"></div>
      <div class="slit"></div>
    </div>
    <div class="panel">
      <div class="ghost-name" aria-hidden="true">Velaski<br>Law Firm</div>
      <div class="pocket"></div>
      <div class="slot">
        <div class="brand"><span class="mark"></span>Velaski Law Firm</div>
        <small>Tomas Edgar Velaski<br>Attorney / Abogado</small>
      </div>
    </div>
  </section>
  <div class="caption" style="left:866px;top:304px;width:312px">Folder Inside</div>

</body>
</html>
```